Fermoso Habitar Presentation

We already have a logo, and now we need a good presentation for our company. You can seach for us at : fermosohabitar.pt and see more about us. We work in adaptive reuse of buildings. You can ask anything you need to do a great job.

Industry/Entity Type

It Company

```html
<!DOCTYPE html>
<html lang="pt">
<head>
<meta charset="utf-8">
<title>Fermoso Habitar – Apresentação</title>
<link href="https://fonts.googleapis.com/css2?family=Arimo:wght@400;700&display=swap" rel="stylesheet">
<style>
  :root{
    --board:#6a6a6a;
    --paper:#ffffff;
    --brand-blue:#2f6bb5;
    --ink:#222222;
    --body:#555555;
    --muted:#9a9a9a;
    --rule:#b5b5b5;
    --bar-dark:#2a2a2a;
    --bar-grey:#a9a9a9;
    --icon-light:#8fb0da;
    --icon-mid:#6a91c8;
    --icon-dark:#2e62ad;
    --note-box:#3e5778;
  }
  *{margin:0;padding:0;box-sizing:border-box}
  html,body{width:1012px;height:1200px;overflow:hidden}
  body{background:var(--board);font-family:"Arimo",Arial,sans-serif;color:var(--body);position:relative}

  .slide{position:absolute;width:452px;height:255px;background:var(--paper);overflow:hidden;box-shadow:0 2px 4px rgba(0,0,0,.35)}
  .photo{position:absolute}

  /* content slide bars */
  .bar-top{position:absolute;left:0;top:0;width:100%;height:5px;
    background:linear-gradient(90deg,var(--bar-dark) 0 35px,var(--brand-blue) 35px 155px,var(--bar-grey) 155px)}
  .bar-bottom{position:absolute;left:0;bottom:0;width:100%;height:4px;
    background:linear-gradient(90deg,var(--bar-grey) 0 297px,var(--brand-blue) 297px 412px,var(--bar-grey) 412px)}

  .footer-page{position:absolute;left:17px;top:235px;font-size:6.5px;color:var(--ink)}
  .footer-divider{position:absolute;left:33px;top:232px;width:1px;height:12px;background:var(--rule)}
  .footer-url{position:absolute;left:41px;top:235px;font-size:6.5px;color:var(--ink);letter-spacing:.2px}
  .footer-url b{font-weight:700}

  .brand{position:absolute;display:flex;align-items:center;gap:4px;font-size:11px;font-weight:700;color:var(--brand-blue);white-space:nowrap}
  .brand-dot{width:10px;height:10px;border-radius:50%;background:var(--brand-blue)}
  .brand.on-dark{color:#ffffff}
  .brand.on-dark .brand-dot{background:#ffffff}
  .brand.footer-brand{right:16px;top:229px}

  .title{position:absolute;left:32px;top:18px;font-size:16.5px;font-weight:700;color:var(--ink);letter-spacing:.2px}
  .title span{color:var(--brand-blue)}
  .title.blue{color:var(--brand-blue)}
  .lede{position:absolute;left:32px;top:38px;font-size:7.2px;color:var(--ink)}
  .lede-rule{position:absolute;left:32px;height:1px;background:#d0d0d0}
  .para{position:absolute;font-size:6.6px;line-height:9.3px;color:var(--body)}
  .tiny{position:absolute;font-size:4.8px;line-height:7px;color:var(--body);text-align:center}

  /* cover */
  .cover-title{position:absolute;right:12px;top:183px;font-size:16px;color:var(--muted);font-weight:700;text-align:right}
  .cover-sub{position:absolute;right:12px;top:203px;font-size:10px;color:var(--muted);font-weight:700}
  .cover-text{position:absolute;left:302px;top:222px;width:140px;font-size:6.4px;line-height:8.5px;color:var(--ink)}
  .slogan{position:absolute;left:34px;top:74px;font-size:11px;font-weight:700;color:#fff;line-height:15px;text-align:center}

  /* hero slides */
  .hero-head{position:absolute;left:20px;top:22px;font-size:16px;font-weight:700;color:#fff}
  .hero-sub{position:absolute;left:20px;top:45px;font-size:10px;font-weight:700;color:#fff}
  .hero-text{position:absolute;left:20px;top:61px;width:120px;font-size:6.4px;line-height:8px;color:#fff}

  /* icon row */
  .pillar{position:absolute;top:98px;width:110px;text-align:center}
  .pillar-disc{width:56px;height:56px;border-radius:50%;margin:0 auto;display:flex;align-items:center;justify-content:center}
  .pillar-name{margin-top:8px;font-size:10.5px;color:var(--ink)}
  .pillar .tiny{position:static;margin-top:6px}

  /* concept note */
  .note-box{position:absolute;left:309px;top:84px;width:106px;height:84px;background:var(--note-box);color:#fff;padding:14px 6px 0;font-size:4.8px;line-height:6.3px;text-align:center}
  .note-badge{position:absolute;left:349px;top:67px;width:25px;height:25px;border-radius:50%;background:var(--note-box);display:flex;align-items:center;justify-content:center}

  .cap{position:absolute;font-size:4.8px;color:var(--body)}
</style>
</head>
<body>

<!-- Slide 1: cover -->
<section class="slide" style="left:30px;top:50px">
  <svg width="452" height="255" viewBox="0 0 452 255" style="position:absolute;left:0;top:0">
    <defs>
      <linearGradient id="cityTone" x1="0" y1="0" x2="1" y2="1">
        <stop offset="0" stop-color="#cfcfcf"/>
        <stop offset=".5" stop-color="#8c8c8c"/>
        <stop offset="1" stop-color="#4a4a4a"/>
      </linearGradient>
    </defs>
    <polygon points="0,0 362,0 232,255 0,255" fill="url(#cityTone)" role="img" aria-label="Black and white photo of dense old city rooftops"/>
    <polygon points="0,0 148,0 186,112 0,112" fill="var(--brand-blue)"/>
    <polygon points="232,255 274,255 274,185" fill="var(--brand-blue)"/>
  </svg>
  <div class="slogan">Slogan Goes Here!!!<br>Slogan Goes Here!!!</div>
  <div class="brand" style="right:12px;top:30px"><span class="brand-dot"></span>Fermoso Habitar</div>
  <div class="cover-title">Title of Presentation</div>
  <div class="cover-sub">Subtitle of Presentation</div>
  <div class="cover-text">Text : Desde 2002 que concebemos, desenvolvemos e gerimos novas soluções de ocu-</div>
</section>

<!-- Slide 2: hero with planning team -->
<section class="slide" style="left:528px;top:50px">
  <div class="photo" role="img" aria-label="Photo of engineers in yellow hard hats reviewing building plans on a table"
       style="inset:0;background:linear-gradient(120deg,#3a4a5e 0%,#8fa2b8 30%,#eef0f2 55%,#f2d23a 80%,#e9e3d8 100%)"></div>
  <svg width="452" height="255" viewBox="0 0 452 255" style="position:absolute;left:0;top:0">
    <polygon points="0,0 268,0 0,190" fill="rgba(25,30,40,.6)"/>
  </svg>
  <div class="hero-head">Heading Goes Here</div>
  <div class="hero-sub">Subtitle of Presentation</div>
  <div class="hero-text">Text : Desde 2002 que concebemos, desenvolvemos e gerimos novas soluções de ocupação</div>
  <div class="brand footer-brand"><span class="brand-dot"></span>Fermoso Habitar</div>
</section>

<!-- Slide 3: about us with street views -->
<section class="slide" style="left:30px;top:341px">
  <div class="bar-top"></div>
  <div class="title">ABOUT <span>US</span></div>
  <div class="lede">Text : Desde 2002 que concebemos,</div>
  <div class="lede-rule" style="top:49px;width:175px"></div>
  <p class="para" style="left:30px;top:64px;width:150px">Text : Desde 2002 que concebemos, desenvolvemos e gerimos novas soluções de ocupação Text : Desde 2002 que concebemos, desenvolvemos e gerimos novas soluções de ocupação Text : Desde 2002 que concebemos, desenvolvemos e gerimos novas soluções de ocupação Text : Desde 2002 que concebemos, desenvolvemos e gerimos novas soluções de ocupação</p>
  <p class="para" style="left:30px;top:170px;width:150px">Text : Desde 2002 que concebemos, desenvolvemos e gerimos novas soluções de ocupação Text : Desde 2002 que concebemos, desenvolvemos e gerimos novas soluções</p>
  <div class="photo" role="img" aria-label="Photo of a historic facade with trees" style="left:230px;top:43px;width:62px;height:162px;background:linear-gradient(180deg,#a9c6e4,#c9b9a0 50%,#5f7a45)"></div>
  <div class="photo" role="img" aria-label="Photo of an ornate city hall tower" style="left:297px;top:43px;width:63px;height:162px;background:linear-gradient(180deg,#b7cfe8,#cdbfa8 45%,#8a7f70)"></div>
  <div class="photo" role="img" aria-label="Photo of a square with a statue and old buildings" style="left:366px;top:43px;width:66px;height:162px;background:linear-gradient(180deg,#9ec0e4,#b9b2a6 55%,#6e6a62)"></div>
  <div class="footer-page">01</div><div class="footer-divider"></div>
  <div class="footer-url">WWW. <b>FERMOSOHABITAR</b>.PT</div>
  <div class="brand footer-brand"><span class="brand-dot"></span>Fermoso Habitar</div>
  <div class="bar-bottom"></div>
</section>

<!-- Slide 4: text with glass facade -->
<section class="slide" style="left:528px;top:341px">
  <div class="bar-top"></div>
  <div class="lede" style="left:30px">Text : Desde 2002 que concebemos, desenvolvemos e gerimos</div>
  <div class="lede-rule" style="left:30px;top:48px;width:228px"></div>
  <p class="para" style="left:30px;top:64px;width:240px">Text : Desde 2002 que concebemos, desenvolvemos e gerimos novas soluções de ocupação Text : Desde 2002 que concebemos, desenvolvemos e gerimos novas soluções de ocupação Text : Desde 2002 que concebemos, desenvolvemos e gerimos novas soluções de ocupação Text : Desde 2002 que concebemos, desenvolvemos e gerimos novas soluções de ocupação</p>
  <p class="para" style="left:30px;top:137px;width:240px">Text : Desde 2002 que concebemos, desenvolvemos e gerimos novas soluções de ocupação Text : Desde 2002 que concebemos, desenvolvemos e gerimos novas soluções de ocupação Text : Desde 2002 que concebemos, desenvolvemos e gerimos novas soluções de ocupação</p>
  <p class="para" style="left:30px;top:183px;width:240px">Text : Desde 2002 que concebemos, desenvolvemos e gerimos novas soluções de ocupação Text : Desde 2002 que concebemos, desenvolvemos e gerimos novas soluções de ocupação Text : Desde 2002 que</p>
  <div style="position:absolute;left:285px;top:41px;width:143px;height:98px;border:1px solid #d6d6d6"></div>
  <div class="photo" role="img" aria-label="Photo looking up at a modern glass office tower" style="left:287px;top:43px;width:139px;height:94px;background:linear-gradient(135deg,#e3eef6,#5a8fb4 45%,#1f4c6e 75%,#a9cde2)"></div>
  <div class="tiny" style="left:366px;top:153px;width:70px">mos, desenvolvemos e gerimos novas soluções de ocupa-ção Text : Desde 2002</div>
  <div class="footer-page">01</div><div class="footer-divider"></div>
  <div class="footer-url">WWW. <b>FERMOSOHABITAR</b>.PT</div>
  <div class="brand footer-brand"><span class="brand-dot"></span>Fermoso Habitar</div>
  <div class="bar-bottom"></div>
</section>

<!-- Slide 5: about us pillars -->
<section class="slide" style="left:30px;top:632px">
  <div class="bar-top"></div>
  <div class="title">ABOUT <span>US</span></div>
  <div class="lede">Text : Desde 2002 que concebemos, desenvolvemos e gerimos</div>
  <div class="lede-rule" style="top:49px;width:226px"></div>
  <p class="para" style="left:30px;top:61px;width:395px">Text : Desde 2002 que concebemos, desenvolvemos e gerimos novas soluções de ocupação Text : Desde 2002 que concebemos, desenvolvemos e gerimos novas soluções de ocupação Text : Desde 2002 que concebemos, desen-</p>

  <div class="pillar" style="left:43px">
    <div class="pillar-disc" style="background:var(--icon-light)">
      <svg width="28" height="28" viewBox="0 0 28 28" fill="none" stroke="#fff" stroke-width="1.4" stroke-linecap="round">
        <path d="M14 7a5.5 5.5 0 0 0-3.3 9.9V19h6.6v-2.1A5.5 5.5 0 0 0 14 7z"/><path d="M11.5 21.5h5M12.5 23.5h3"/>
        <path d="M14 2.5v2M5 6l1.5 1.5M23 6l-1.5 1.5M3 13h2M23 13h2"/>
      </svg>
    </div>
    <div class="pillar-name">CONCEITO</div>
    <div class="tiny">mos, desenvolvemos<br>e gerimos novas<br>soluções de ocupa-</div>
  </div>
  <div class="pillar" style="left:170px">
    <div class="pillar-disc" style="background:var(--icon-mid)">
      <svg width="28" height="28" viewBox="0 0 28 28" fill="#fff">
        <rect x="13" y="3" width="2" height="5"/><rect x="11.5" y="4.5" width="5" height="2"/>
        <path d="M10.5 9h7l-1.5 4h-4z"/><path d="M12 13h4l1 8h-6z"/><rect x="9" y="21" width="10" height="3" rx="1"/>
      </svg>
    </div>
    <div class="pillar-name">DESENVOLVIMENTO</div>
    <div class="tiny">mos, desenvolvemos<br>e gerimos novas<br>soluções de ocupa-</div>
  </div>
  <div class="pillar" style="left:296px">
    <div class="pillar-disc" style="background:var(--icon-dark)">
      <svg width="28" height="28" viewBox="0 0 28 28" fill="none" stroke="#fff" stroke-width="1.5" stroke-linejoin="round">
        <path d="M18 4l5 5-11 11-6 2 2-6z"/><path d="M16 6l5 5M8 16l4 4"/>
      </svg>
    </div>
    <div class="pillar-name">GESTÃO</div>
    <div class="tiny">mos, desenvolvemos<br>e gerimos novas<br>soluções de ocupa-</div>
  </div>

  <div class="footer-page">01</div><div class="footer-divider"></div>
  <div class="footer-url">WWW. <b>FERMOSOHABITAR</b>.PT</div>
  <div class="brand footer-brand"><span class="brand-dot"></span>Fermoso Habitar</div>
  <div class="bar-bottom"></div>
</section>

<!-- Slide 6: concept -->
<section class="slide" style="left:528px;top:632px">
  <div class="bar-top"></div>
  <div class="title blue" style="left:31px">CONCEITO</div>
  <div class="lede" style="left:31px">Text : Desde 2002 que concebemos, desenvolvemos e gerimos</div>
  <div class="lede-rule" style="left:31px;top:49px;width:226px"></div>
  <div class="photo" role="img" aria-label="Photo of a hand drafting with a scale ruler on architectural plans" style="left:33px;top:67px;width:224px;height:68px;background:linear-gradient(100deg,#eef1f4,#c9d2dc 45%,#e9ddd0 75%,#b9b2aa)"></div>
  <p class="para" style="left:31px;top:177px;width:262px">Text : Desde 2002 que concebemos, desenvolvemos e gerimos novas soluções de ocupação Text : Desde 2002 que concebemos, desenvolvemos e gerimos novas soluções de ocupação Text : Desde 2002 que concebemos, desenvolvemos e gerimos novas soluções de ocupação Text : Desde 2002</p>
  <div class="note-box">Text : Desde 2002 que concebemos, desenvolvemos e gerimos novas soluções de ocupação Text : Desde 2002 que concebemos, desenvolvemos e gerimos novas soluções de ocupação Text : Desde 2002 que concebemos, desenvolvemos e gerimos novas soluções de ocupação<br><br>Text : Desde 2002 que concebe-</div>
  <div class="note-badge">
    <svg width="14" height="14" viewBox="0 0 28 28" fill="none" stroke="#fff" stroke-width="2" stroke-linecap="round">
      <path d="M14 7a5.5 5.5 0 0 0-3.3 9.9V19h6.6v-2.1A5.5 5.5 0 0 0 14 7z"/><path d="M11.5 22h5"/>
      <path d="M14 2v2M5 6l1.5 1.5M23 6l-1.5 1.5"/>
    </svg>
  </div>
  <div class="footer-page">01</div><div class="footer-divider"></div>
  <div class="footer-url">WWW. <b>FERMOSOHABITAR</b>.PT</div>
  <div class="brand footer-brand"><span class="brand-dot"></span>Fermoso Habitar</div>
  <div class="bar-bottom"></div>
</section>

<!-- Slide 7: hero with evening plaza -->
<section class="slide" style="left:30px;top:908px">
  <div class="photo" role="img" aria-label="Evening photo of a modern angular canopy over a café terrace beside a historic church tower"
       style="inset:0;background:linear-gradient(160deg,#2d2a26 0%,#4f5f86 35%,#c79a5c 60%,#6a4a2a 85%,#2a1e16 100%)"></div>
  <svg width="452" height="255" viewBox="0 0 452 255" style="position:absolute;left:0;top:0">
    <polygon points="0,0 250,0 0,175" fill="rgba(20,18,16,.55)"/>
  </svg>
  <div class="hero-head">Heading Goes Here</div>
  <div class="hero-sub">Subtitle of Presentation</div>
  <div class="hero-text">Text : Desde 2002 que concebemos, desenvolvemos e gerimos novas soluções de ocupação</div>
  <div class="brand on-dark footer-brand"><span class="brand-dot"></span>Fermoso Habitar</div>
</section>

<!-- Slide 8: gallery -->
<section class="slide" style="left:528px;top:908px">
  <div class="bar-top"></div>
  <div class="title" style="left:31px">OUR <span>GALLARY</span></div>
  <div class="lede" style="left:31px">Text : Desde 2002 que concebemos, desenvolvemos e gerimos</div>
  <div class="lede-rule" style="left:31px;top:49px;width:226px"></div>
  <div class="cap" style="left:34px;top:61px">mos, desenvolvemos e</div>
  <div class="cap" style="left:127px;top:61px">mos, desenvolvemos e</div>
  <div class="photo" role="img" aria-label="Photo of a campus lawn and building under blue sky" style="left:34px;top:69px;width:85px;height:62px;background:linear-gradient(180deg,#8eb4de,#d8c9a8 55%,#5d8a3c)"></div>
  <div class="photo" role="img" aria-label="Photo of visitors in a bright exhibition hall" style="left:127px;top:69px;width:85px;height:62px;background:linear-gradient(180deg,#d9dde2,#8a8e96 60%,#3f3a38)"></div>
  <div class="photo" role="img" aria-label="Night photo of a lit facade" style="left:34px;top:139px;width:85px;height:62px;background:linear-gradient(160deg,#0f1522,#2d3a5a 50%,#b9a7a0)"></div>
  <div class="photo" role="img" aria-label="Night photo of a crowded street with warm lights" style="left:127px;top:139px;width:85px;height:62px;background:linear-gradient(180deg,#121520,#3a2c22 55%,#c9873a)"></div>
  <div class="photo" role="img" aria-label="Photo of a large ring sculpture inside an exhibition pavilion" style="left:220px;top:69px;width:174px;height:132px;background:linear-gradient(170deg,#6b6b70,#a9a9ae 40%,#5a5e66 75%,#8a8480)"></div>
  <div class="cap" style="left:34px;top:205px">mos, desenvolvemos e</div>
  <div class="cap" style="left:127px;top:205px">mos, desenvolvemos e</div>
  <div class="cap" style="left:220px;top:205px">mos, desenvolvemos e gerimos novas soluções de ocupa-</div>
  <div class="footer-page">01</div><div class="footer-divider"></div>
  <div class="footer-url">WWW. <b>FERMOSOHABITAR</b>.PT</div>
  <div class="brand footer-brand"><span class="brand-dot"></span>Fermoso Habitar</div>
  <div class="bar-bottom"></div>
</section>

</body>
</html>
```